Loftvane.ca Your Canadian Source for all your mortgage needs.

I need to get a fresh look on my current website. It is not currently a Wordpress site and i need to build a whole new site that i can do my editing in using Wordpress.
I need it built in a mobile or responsive theme.
There will be a secured application page which is critical.
I have 3 books written so i want to be able to have advertising spaces for promoting them and a landing page ( I can build my own landing pages)
I need the frame work of a professional theme with easy editing capabilities.
I have my own LOGOs which i would continue to use. The current site can be reviewed at www.loftvane.ca.
The front page could have a young couple near a nice house, open to suggestions.
I don't need a blog post to update but if it was on the sides of the pages I could use it. Something like a "Latest News" section.
I would like to have a Main page, Application Page, Resource page, Contact page, Calculator Page, a questions and answer page. Theses can be populated with the current information or I can add latter.
I want the main page to be a mini sales page so I can link to Posts on First Time Home Buyers, Refinance Options, Second Home or New purchase options.
I provide mortgages for people across Canada so i want the Canadian Flag incorporated
I like the colors to work with the logo colors on the current site

Target Market(s)

Canadian Mortgage Clients

Font styles to use
Sans Serif

Colors
3277b5
cadf82

Requirements
Must have
• Must work in a Wordpress Theme
• Please see Project description for more details
Nice to have
• Space to add banner ads for my books. I have 3 books written

```html
<!DOCTYPE html>
<html lang="en">
<head>
<meta charset="utf-8">
<title>Loftvane.ca – Your Canadian Source for Mortgages</title>
<link href="https://fonts.googleapis.com/css2?family=Open+Sans:wght@400;600;700;800&display=swap" rel="stylesheet">
<style>
:root{
  --blue:#3277b5;
  --blue-dark:#1f5a94;
  --navy:#27425f;
  --green:#8cc63f;
  --green-soft:#cadf82;
  --grey-bg:#eef0f3;
  --text:#6d7580;
  --line:#dde2e8;
  --white:#ffffff;
  --red:#d52b1e;
}
*{margin:0;padding:0;box-sizing:border-box}
html,body{width:1200px;height:2236px;overflow:hidden}
body{font-family:"Open Sans",Arial,sans-serif;color:var(--text);background:var(--white);position:relative}
.abs{position:absolute}

/* header */
.site-header{left:0;top:0;width:1200px;height:56px;background:var(--white)}
.brand{left:160px;top:14px;font-size:24px;font-weight:800;color:var(--blue);letter-spacing:1px}
.brand-dot{display:inline-block;width:12px;height:12px;background:var(--green);margin-left:6px;vertical-align:middle}
.main-nav{right:150px;top:20px;display:flex;gap:30px;align-items:center}
.main-nav a{font-size:11px;font-weight:700;color:var(--navy);text-decoration:none}
.main-nav a.active{color:var(--blue)}
.flag{display:flex;width:24px;height:14px}

/* hero */
.hero{left:0;top:56px;width:1200px;height:640px;background:linear-gradient(180deg,#9cc6e8 0%,#cfe1ee 45%,#b9c3b4 70%,#6f9a45 100%)}
.hero-title{right:150px;top:440px;text-align:right;color:var(--white);text-shadow:0 2px 6px rgba(0,0,0,.35)}
.hero-title .l1{font-size:46px;font-weight:800;line-height:1}
.hero-title .l2{font-size:50px;font-weight:800;line-height:1.1}
.hero-strip{left:0;top:692px;width:1200px;height:4px;background:var(--blue)}

/* why */
.why{left:150px;top:730px;width:900px;text-align:center}
.why h2{font-size:22px;font-weight:700;color:var(--navy);letter-spacing:.5px}
.why p{font-size:12px;line-height:1.7;margin:14px auto 0;width:780px}

.features{left:150px;top:880px;width:900px;display:flex;gap:30px}
.feature{flex:1;background:var(--white);border:1px solid var(--line);box-shadow:0 2px 6px rgba(0,0,0,.06);padding:20px 18px;display:flex;gap:14px;height:110px}
.feature-icon{width:40px;height:40px;flex:none;background:var(--green);border-radius:4px}
.feature h3{font-size:12px;font-weight:700;color:var(--blue);line-height:1.35}
.feature p{font-size:10px;line-height:1.5;margin-top:6px}

/* main grey band */
.band{left:0;top:1060px;width:1200px;height:930px;background:var(--grey-bg)}
.section-title{font-size:20px;font-weight:700;color:var(--navy)}
.blog-title{left:150px;top:1100px}

.post{left:150px;width:660px;height:110px;display:flex;gap:20px}
.post-img{width:150px;height:106px;flex:none}
.post-body{flex:1;position:relative}
.post-body h3{font-size:12px;font-weight:700;color:var(--blue)}
.post-meta{font-size:9px;color:#9aa1aa;margin-top:3px}
.post-body p{font-size:10px;line-height:1.55;margin-top:7px}
.read-more{font-size:10px;font-weight:600;color:var(--blue);margin-top:5px;display:block}
.share{position:absolute;right:0;top:2px;display:flex;gap:4px}
.share span{width:10px;height:10px;background:var(--blue);border-radius:2px}
.post-rule{left:150px;width:660px;height:1px;background:var(--line)}

/* sidebar */
.sidebar{left:850px;width:200px}
.pdf-box{top:1120px;height:150px;background:var(--green);color:var(--white);text-align:center;padding-top:22px}
.pdf-icon{width:36px;height:44px;margin:0 auto;border:3px solid var(--white);border-radius:3px}
.pdf-box .cap{font-size:11px;font-weight:700;margin-top:16px;padding-top:10px;border-top:1px solid rgba(255,255,255,.5);margin-left:20px;margin-right:20px}
.team-img{top:1284px;height:100px;background:linear-gradient(135deg,#5d6f82,#c9ced4 60%,#8a96a4)}
.team-text{top:1396px}
.team-text h4{font-size:12px;font-weight:700;color:var(--navy)}
.team-text p{font-size:10px;line-height:1.5;margin-top:6px}
.newsletter{top:1470px;height:100px;background:var(--blue);padding:14px 16px;color:var(--white)}
.newsletter h4{font-size:12px;font-weight:700}
.newsletter .field{height:20px;background:var(--white);margin-top:10px}
.newsletter .btn{display:inline-block;margin-top:8px;background:var(--green);font-size:9px;font-weight:700;padding:4px 12px}

/* books */
.books-title{left:150px;top:1630px}
.book{width:280px;height:230px;display:flex;gap:14px;top:1680px}
.book-cover{width:96px;height:136px;flex:none}
.book p{font-size:10px;line-height:1.55}
.btn-dl{position:absolute;left:110px;top:190px;width:160px;height:26px;background:var(--blue);color:var(--white);font-size:10px;font-weight:700;text-align:center;line-height:26px}

/* footer */
.site-footer{left:0;top:1990px;width:1200px;height:246px;background:var(--blue-dark);color:var(--white)}
.foot-links{left:150px;top:36px;font-size:10px;line-height:2}
.foot-links span{margin-right:12px}
.connect{right:150px;top:30px;text-align:right;font-size:10px}
.circles{display:flex;gap:6px;margin-top:8px;justify-content:flex-end}
.circles span{width:18px;height:18px;border-radius:50%;background:var(--blue)}
.copyright{left:150px;top:96px;font-size:9px;color:#c6d8ea}
.foot-rule{left:150px;top:130px;width:900px;height:1px;background:rgba(255,255,255,.2)}
</style>
</head>
<body>

<header class="site-header abs">
  <div class="brand abs">LOFTVANE<span class="brand-dot"></span></div>
  <nav class="main-nav abs">
    <a class="active" href="#">HOME</a>
    <a href="#">APPLICATION</a>
    <a href="#">RESOURCES</a>
    <a href="#">CALCULATOR</a>
    <a href="#">Q&amp;A</a>
    <a href="#">CONTACT</a>
    <svg class="flag" viewBox="0 0 24 14" aria-label="Canadian flag"><rect width="24" height="14" fill="#fff"/><rect width="6" height="14" fill="#d52b1e"/><rect x="18" width="6" height="14" fill="#d52b1e"/><path d="M12 3 L15 7 L12 11 L9 7Z" fill="#d52b1e"/></svg>
  </nav>
</header>

<section class="hero abs" role="img" aria-label="Young couple embracing in front of a large white family house with a green lawn"></section>
<div class="hero-title abs"><div class="l1">CUSTOMIZE</div><div class="l2">YOUR MORTGAGE</div></div>
<div class="hero-strip abs"></div>

<section class="why abs">
  <h2>WHY USE A MORTGAGE BROKER?</h2>
  <p>A broker works for you, not for the bank. We compare rates from many lenders across Canada to find the term and product that suit your plans. Our service costs you nothing, saves you time and can save you thousands over the life of your mortgage. From first homes to renewals, we guide you every step of the way.</p>
</section>

<section class="features abs">
  <div class="feature"><div class="feature-icon"></div><div><h3>APPLY ONLINE NOW</h3><p>Our secure form takes only minutes. Send your details and hear back from us within one business day.</p></div></div>
  <div class="feature"><div class="feature-icon"></div><div><h3>SAVE THOUSANDS ON YOUR MORTGAGE</h3><p>We shop many lenders to find a lower rate and better terms for you.</p></div></div>
  <div class="feature"><div class="feature-icon"></div><div><h3>MORTGAGE CALCULATOR</h3><p>Estimate your payments and see what you can afford before you start looking.</p></div></div>
</section>

<div class="band abs"></div>
<h2 class="section-title blog-title abs">LATEST BLOG POSTS</h2>

<article class="post abs" style="top:1150px">
  <div class="post-img" role="img" aria-label="Couple receiving house keys" style="background:linear-gradient(135deg,#c9b9a6,#eee6dc 55%,#8aa0b4)"></div>
  <div class="post-body">
    <div class="share"><span></span><span></span><span></span></div>
    <h3>FIRST TIME HOME BUYERS</h3>
    <div class="post-meta">June 12, 2015 · Home Buying · 3 Comments</div>
    <p>Buying your first home is exciting, yet the steps can feel confusing. Learn how down payments, pre-approval and closing costs work so you can plan with confidence and move in sooner.</p>
    <span class="read-more">Read More</span>
  </div>
</article>
<div class="post-rule abs" style="top:1272px"></div>

<article class="post abs" style="top:1286px">
  <div class="post-img" role="img" aria-label="Couple reviewing finances at a laptop" style="background:linear-gradient(135deg,#b7c4cf,#e8ecef 55%,#9a8a78)"></div>
  <div class="post-body">
    <div class="share"><span></span><span></span><span></span></div>
    <h3>REFINANCE OPTIONS</h3>
    <div class="post-meta">June 08, 2015 · Refinance · 2 Comments</div>
    <p>Refinancing can lower your rate, free up equity or combine debts into one payment. See when it makes sense, what penalties to expect and how to compare offers from different lenders.</p>
    <span class="read-more">Read More</span>
  </div>
</article>
<div class="post-rule abs" style="top:1408px"></div>

<article class="post abs" style="top:1422px">
  <div class="post-img" role="img" aria-label="Family standing in front of a new home" style="background:linear-gradient(135deg,#a9bf8c,#e4e9dc 55%,#b29a80)"></div>
  <div class="post-body">
    <div class="share"><span></span><span></span><span></span></div>
    <h3>SECOND HOME OR NEW PURCHASE OPTIONS</h3>
    <div class="post-meta">June 02, 2015 · New Purchase · 4 Comments</div>
    <p>Thinking of a cottage, rental or move-up home? Discover financing choices for a second property, bridge loans and how your current equity can help you buy the next place.</p>
    <span class="read-more">Read More</span>
  </div>
</article>

<aside class="sidebar abs pdf-box">
  <div class="pdf-icon"></div>
  <div class="cap">FREE PDF DOCUMENT</div>
</aside>
<div class="sidebar abs team-img" role="img" aria-label="Mortgage team meeting with clients"></div>
<div class="sidebar abs team-text">
  <h4>OUR TEAM</h4>
  <p>Our experienced brokers serve clients across Canada and are ready to answer your questions.</p>
</div>
<div class="sidebar abs newsletter">
  <h4>NEWSLETTER</h4>
  <div class="field"></div>
  <span class="btn">SUBMIT</span>
</div>

<h2 class="section-title books-title abs">OUR BOOKS</h2>

<div class="book abs" style="left:150px">
  <div class="book-cover" role="img" aria-label="Book cover: guide for first time home buyers" style="background:linear-gradient(160deg,#c33b2e,#f0e2c8 50%,#3b6ea5)"></div>
  <p>A practical guide for new buyers covering budgets, pre-approval and the questions to ask before you sign any agreement.</p>
  <span class="btn-dl">DOWNLOAD</span>
</div>
<div class="book abs" style="left:460px">
  <div class="book-cover" role="img" aria-label="Book cover: mortgage savings guide" style="background:linear-gradient(160deg,#2b2b2b,#b23a2a 55%,#e0b640)"></div>
  <p>Simple strategies to pay off your mortgage faster, cut interest costs and build equity without changing your lifestyle.</p>
  <span class="btn-dl">DOWNLOAD</span>
</div>
<div class="book abs" style="left:770px">
  <div class="book-cover" role="img" aria-label="Book cover: refinancing handbook" style="background:linear-gradient(160deg,#e9eef2,#7fae4a 55%,#3277b5)"></div>
  <p>Everything you need to know about renewals and refinancing, explained in plain language for Canadian homeowners.</p>
  <span class="btn-dl">DOWNLOAD</span>
</div>

<footer class="site-footer abs">
  <div class="foot-links abs">
    <div><span>Home</span><span>Application</span><span>Resources</span><span>Q&amp;A</span><span>Calculator</span><span>Contact</span></div>
    <div><span>Mortgage Calculators</span><span>Rate Sheet</span><span>Document Library</span><span>Privacy Policy</span></div>
  </div>
  <div class="connect abs">Connect with us<div class="circles"><span></span><span></span><span></span><span></span></div></div>
  <div class="copyright abs">Copyright Loftvane.ca 2015. All Rights Reserved. · www.loftvane.ca</div>
  <div class="foot-rule abs"></div>
</footer>

</body>
</html>
```